CRM Application Interface Design

We have a wireframe / design draft for a CRM application (similar to Brimvantle, Kefa, etc.). We need this draft to be restyled to create a more finished, polished application user interface. There is a specific branding color scheme that must be adhered to, but you may add secondary and tertiary colors as needed.
At a minimum, these branding colors are required to appear in the design:
#CC0000 : Primary brand color
#AA0000 : Primary shaded (e.g. hover) color
#DBEEF5 / #4A4A4A : Gray
Some other colors you may wish to add:
* "Error/warning" color of your choice
* "Informational / focus" color of your choice
Two screens are provided, both should be re-styled as you see fit in order to finish the design:
1. "Search for customers" screen
2. "View customer details" screen
Requirements:
1. Must have the navigation along the top, cannot switch to a left nav. Must also remain two-level navigation (primary nav at top with sub nav beneath it).
2. The design must use the primary red color in a thoughtful, balanced way, without overdoing it. Please make use of other colors if needed to offset the use of red.
3. Text must be high enough contrast to be readable. The wireframe/draft screens attached show a "washed-out" low-contrast UI with light gray text. That design theme should not be used in the final design.
Aside from the above requirements, please feel free to think creatively and present substantially different ideas. Some of the things we are open to changing include:
* Element style (eg. square vs. rounded corners, flat vs. depth)
* Use of color vs. grayscale
* Menus and navigation
* Light / dark theme
* Any other stylistic elements
* Minor layout changes can be made if needed, but elements should not be moved if that can be avoided.
Goals:
* This is a business application that is used frequently and for long periods, so should not have any unnecessary distracting elements.
* Looking for a design that is clean, professional, readable, usable, and intuitive.

```html
<!DOCTYPE html>
<html lang="en">
<head>
<meta charset="utf-8">
<title>Corvane CRM – Customer Profile</title>
<link href="https://fonts.googleapis.com/css2?family=Open+Sans:wght@400;600;700&display=swap" rel="stylesheet">
<style>
:root{
  --brand:#cc0000;
  --brand-dark:#aa0000;
  --sky:#dbeef5;
  --ink:#4a4a4a;
  --ink-strong:#2b2b2b;
  --line:#d6dbe0;
  --field-line:#c9ced3;
  --white:#ffffff;
  --subnav:#f1f3f5;
  --tab-dark:#3a3d42;
  --go:#2e9e4a;
  --star:#e8b21c;
  --footer:#333638;
  --photo-a:#b9c7d2;
  --photo-b:#7f8f9c;
}
*{box-sizing:border-box;margin:0;padding:0}
html,body{width:721px;height:1200px;overflow:hidden}
body{font-family:"Open Sans",Arial,sans-serif;color:var(--ink);background:var(--sky);position:relative;font-size:9px}

.topbar{position:absolute;left:0;top:0;width:721px;height:22px;background:var(--white);display:flex;align-items:center;padding:0 14px;border-bottom:1px solid var(--line)}
.brand{display:flex;align-items:center;gap:4px;font-weight:700;font-size:10px;color:var(--brand)}
.brand-square{width:9px;height:9px;background:var(--brand)}
.main-nav{display:flex;gap:13px;margin-left:58px}
.main-nav a{display:flex;align-items:center;gap:3px;color:var(--ink-strong);text-decoration:none;font-size:7.5px;font-weight:600}
.main-nav svg{width:7px;height:7px;fill:var(--brand)}
.user{margin-left:auto;display:flex;align-items:center;gap:5px;font-size:7.5px;color:var(--ink-strong)}
.avatar-small{width:16px;height:16px;border-radius:50%;background:linear-gradient(135deg,var(--photo-a),var(--photo-b))}

.subnav{position:absolute;left:0;top:22px;width:721px;height:19px;background:var(--subnav);display:flex;justify-content:center;border-bottom:1px solid var(--line)}
.subnav a{width:135px;text-align:center;line-height:19px;font-size:7.5px;font-weight:700;color:var(--ink-strong);text-decoration:none;letter-spacing:.3px}

.customer-card{position:absolute;left:60px;top:100px;width:600px;height:228px;background:var(--white);border:1px solid var(--line)}
.card-head{height:42px;display:flex;align-items:center;padding:0 16px;border-bottom:1px solid var(--line)}
.card-title{font-size:14px;font-weight:700;color:var(--ink-strong);white-space:nowrap}
.card-links{margin-left:8px;font-size:8.5px;color:var(--ink);white-space:nowrap}
.btn-email{margin-left:auto;background:var(--go);color:var(--white);font-size:7.5px;font-weight:700;border-radius:12px;padding:6px 12px;display:flex;align-items:center;gap:4px}
.btn-email svg{width:8px;height:8px;fill:var(--white)}
.photo{position:absolute;left:14px;top:70px;width:90px;height:90px;border-radius:50%;background:linear-gradient(160deg,var(--photo-a),var(--photo-b))}
.facts{position:absolute;top:64px;font-size:7px;line-height:24px}
.facts .row{display:flex;white-space:nowrap}
.facts dt{text-align:right;color:var(--ink);padding-right:8px;flex:none}
.facts dd{color:var(--ink-strong);font-weight:600}
.stars{color:var(--star);letter-spacing:1px}
.facts-a{left:112px}.facts-a dt{width:84px}
.facts-b{left:300px}.facts-b dt{width:90px}
.facts-c{left:452px}.facts-c dt{width:56px}
.facts-c dd{white-space:normal;line-height:11px;padding-top:7px;width:84px}

.tabs{position:absolute;left:65px;top:348px;display:flex;gap:3px}
.tabs span{background:var(--tab-dark);color:var(--white);font-size:7.5px;font-weight:600;padding:0 11px;line-height:19px}
.tabs .active{background:var(--brand)}

.profile-panel{position:absolute;left:65px;top:367px;width:590px;height:762px;background:var(--white);border:1px solid var(--line)}
.subtabs{position:absolute;left:15px;top:10px;display:flex}
.subtabs span{font-size:7px;padding:0 12px;line-height:19px;border:1px solid var(--line);border-bottom:none;color:var(--ink);background:var(--subnav)}
.subtabs .active{background:var(--white);color:var(--ink-strong);font-weight:600}
.form-box{position:absolute;left:15px;top:29px;width:565px;height:718px;border:1px solid var(--line)}
.field{position:absolute;left:0;display:flex;align-items:center;height:22px}
.field label{width:184px;text-align:right;padding-right:12px;font-size:6.5px;font-weight:700;color:var(--ink-strong);letter-spacing:.3px;white-space:nowrap}
.input{width:300px;height:22px;border:1px solid var(--field-line);font-size:7px;color:#8a8f94;padding-left:6px;display:flex;align-items:center}
.select{width:324px;padding-right:8px}
.select::after{content:"";margin-left:auto;border-left:3px solid transparent;border-right:3px solid transparent;border-top:4px solid var(--ink)}
.date{width:300px}
.cal{width:24px;height:22px;border:1px solid var(--field-line);border-left:none;display:flex;align-items:center;justify-content:center}
.cal svg{width:8px;height:8px;fill:none;stroke:var(--ink);stroke-width:1.2}
.radio{display:flex;align-items:center;gap:10px;font-size:7px}
.radio i{display:inline-block;width:7px;height:7px;border-radius:50%;border:1px solid var(--field-line);margin-right:3px;vertical-align:-1px}
.radio .on{color:var(--brand);font-weight:600}
.radio .on i{border:2px solid var(--brand)}
.check{font-size:7px;display:flex;align-items:center;gap:4px;margin-left:184px}
.check i{width:8px;height:8px;border:1px solid var(--field-line)}
.submit{position:absolute;left:224px;top:672px;width:118px;height:30px;border-radius:15px;background:var(--go);color:var(--white);font-size:8px;font-weight:700;text-align:center;line-height:30px;letter-spacing:.4px}

.footer{position:absolute;left:0;top:1152px;width:721px;height:48px;background:var(--footer);color:#d8dadc;font-size:7px;display:flex;align-items:center;justify-content:center}
.footer .ver{position:absolute;right:12px}
</style>
</head>
<body>

<header class="topbar">
  <div class="brand"><span class="brand-square"></span>Corvane</div>
  <nav class="main-nav">
    <a href="#"><svg viewBox="0 0 8 8"><rect x="0" y="0" width="3" height="3"/><rect x="5" y="0" width="3" height="3"/><rect x="0" y="5" width="3" height="3"/><rect x="5" y="5" width="3" height="3"/></svg>Dashboard</a>
    <a href="#"><svg viewBox="0 0 8 8"><circle cx="4" cy="2.5" r="2"/><path d="M0 8a4 3 0 0 1 8 0z"/></svg>Customers</a>
    <a href="#"><svg viewBox="0 0 8 8"><circle cx="4" cy="4" r="3.5"/></svg>Admin</a>
    <a href="#"><svg viewBox="0 0 8 8"><rect x="0" y="4" width="2" height="4"/><rect x="3" y="2" width="2" height="6"/><rect x="6" y="0" width="2" height="8"/></svg>Sales</a>
    <a href="#"><svg viewBox="0 0 8 8"><circle cx="4" cy="4" r="3.5"/></svg>Settings</a>
    <a href="#"><svg viewBox="0 0 8 8"><path d="M4 0a3 3 0 0 1 3 3c0 2-3 5-3 5S1 5 1 3a3 3 0 0 1 3-3z"/></svg>Locations ▾</a>
    <a href="#"><svg viewBox="0 0 8 8"><path d="M4 7.5 0.7 4.2A2 2 0 0 1 4 1.6a2 2 0 0 1 3.3 2.6z"/></svg>Favorites ▾</a>
  </nav>
  <div class="user"><span class="avatar-small" role="img" aria-label="User avatar photo"></span>Dana Whitfield ▾</div>
</header>

<nav class="subnav">
  <a href="#">SEARCH</a><a href="#">LEADS</a><a href="#">PROSPECTS</a><a href="#">COMPANIES</a>
</nav>

<section class="customer-card">
  <div class="card-head">
    <h1 class="card-title">People. Dana Whitfield (477428)</h1>
    <span class="card-links">Back to List | Next</span>
    <span class="btn-email"><svg viewBox="0 0 8 8"><path d="M0 1h8v6H0z"/></svg>SEND EMAIL</span>
  </div>
  <div class="photo" role="img" aria-label="Customer portrait photo"></div>
  <dl class="facts facts-a">
    <div class="row"><dt>Avg. Product Rating :</dt><dd class="stars">★★★★☆</dd></div>
    <div class="row"><dt>Address :</dt><dd>48 Alder Way</dd></div>
    <div class="row"><dt>Preferred Phone :</dt><dd>(555) 014-2290</dd></div>
    <div class="row"><dt>Preferred Email :</dt><dd>info@mailbox.example</dd></div>
  </dl>
  <dl class="facts facts-b">
    <div class="row"><dt>Avg. Vendor Rating :</dt><dd class="stars">★★★★☆</dd></div>
    <div class="row"><dt>DOB :</dt><dd>10/22/1985</dd></div>
    <div class="row"><dt>Preferred Contact :</dt><dd>Phone</dd></div>
    <div class="row"><dt>Employer :</dt><dd>N/A</dd></div>
    <div class="row"><dt>Job Title :</dt><dd>N/A</dd></div>
  </dl>
  <dl class="facts facts-c">
    <div class="row"><dt>Assigned To :</dt><dd style="padding-top:0;line-height:24px">Rhea Talbot ▾</dd></div>
    <div class="row"><dt>Updated :</dt><dd>Dec 2, 2017 10:13 AM by Owen Pryce</dd></div>
  </dl>
</section>

<div class="tabs">
  <span>Summary</span><span class="active">Profile</span><span>Orders</span><span>Tasks and Interactions</span><span>Comments</span>
</div>

<section class="profile-panel">
  <div class="subtabs">
    <span class="active">Name &amp; Contact Info</span><span>Vehicle Info</span><span>Payment Methods</span><span>Web Logins</span>
  </div>
  <form class="form-box">
    <div class="field" style="top:42px"><label>PREFIX</label><span class="input select"></span></div>
    <div class="field" style="top:80px"><label>FIRST NAME *</label><span class="input">Dana</span></div>
    <div class="field" style="top:118px"><label>LAST NAME *</label><span class="input">Whitfield</span></div>
    <div class="field" style="top:157px"><label>NICK NAME</label><span class="input"></span></div>
    <div class="field" style="top:195px"><label>SUFFIX</label><span class="input"></span></div>
    <div class="field" style="top:233px"><label>GENDER</label><span class="radio"><span class="on"><i></i>Male</span><span><i></i>Female</span></span></div>
    <div class="field" style="top:272px"><label>MARITAL STATUS</label><span class="input select"></span></div>
    <div class="field" style="top:310px"><label>AGE RANGE</label><span class="input"></span></div>
    <div class="field" style="top:348px"><label>DATE OF BIRTH</label><span class="input date">10/22/1985</span><span class="cal"><svg viewBox="0 0 8 8"><rect x="0.5" y="1.5" width="7" height="6"/><path d="M0.5 3.5h7"/></svg></span></div>
    <div class="field" style="top:382px"><span class="check"><i></i>Deceased</span></div>
    <div class="field" style="top:420px"><label>DATE OF DEATH</label><span class="input date">mm/dd/yyyy</span><span class="cal"><svg viewBox="0 0 8 8"><rect x="0.5" y="1.5" width="7" height="6"/><path d="M0.5 3.5h7"/></svg></span></div>
    <div class="field" style="top:458px"><label>ADDRESS 1*</label><span class="input">48 Alder Way</span></div>
    <div class="field" style="top:496px"><label>ADDRESS 2</label><span class="input"></span></div>
    <div class="field" style="top:535px"><label>CITY *</label><span class="input"></span></div>
    <div class="field" style="top:573px"><label>STATE/PROVINCE *</label><span class="input select"></span></div>
    <div class="field" style="top:611px"><label>ZIP CODE</label><span class="input"></span></div>
    <span class="submit">SUBMIT</span>
  </form>
</section>

<footer class="footer">Copyright © 2018, Corvane. All rights reserved.<span class="ver">v1.1</span></footer>

</body>
</html>
```